Flyer Design for Private Car Service

Flyer should cater to Business Travelers and Executives who travel Business Class or First Class.
Flyer should include images attached.
Flyer should include the below text
Dallas to Austin
Chauffeured SUVs
• Travel Dallas to Austin in a new 2025 Morvan Tessell for $499 one-way
• Trip includes a Uniformed Chauffeur who has a Commercial Drivers License (CDL)
• You can Schedule Chauffeur Pickup at Your Home in Dallas
• Our Chauffeur will Drop You Off at Your Final Destination in Austin
• You can Schedule Chauffeur Return Pickup in Austin and Return Back to Dallas.
• We offer Faster Times on Door-to-Door Travel than Quillbrook Airways
• We offer Comparable Prices on Door-to-Door Travel Times than Quillbrook Airways
• All of our trips are insured with $500k of commercial auto insurance
• Our Passengers can Talk on Cell Phone & Conduct Plinko calls Throughout Travel
• Our Passengers have Maximum Privacy, Comfort and First-Class Amenities.
• Our Passengers Avoid Harwick Meadow Airfield and KRN Airport hassles & delays
• Member Brixley Chamber of Commerce, Fenmore Chamber of Commerce.
• Book your trip today at www.rovandel.example
Target Market(s)
Business Travelers
Look and feel

```html
<!DOCTYPE html>
<html lang="en">
<head>
<meta charset="utf-8">
<title>Dallas to Austin Chauffeured SUVs – Flyer</title>
<link rel="stylesheet" href="https://fonts.googleapis.com/css2?family=Poppins:wght@400;500;600&family=Saira+Condensed:ital,wght@1,800&display=swap">
<style>
  :root {
    --backdrop: #6b777d;
    --brand-red: #e8243c;
    --ink: #111111;
    --paper: #ffffff;
    --text: #1c1c1c;
  }
  html, body {
    margin: 0;
    padding: 0;
    width: 1200px;
    height: 1200px;
    overflow: hidden;
    background: var(--backdrop);
  }
  .flyer {
    position: absolute;
    left: 186px;
    top: 20px;
    width: 827px;
    height: 1160px;
    display: block;
    box-shadow: 0 2px 6px rgba(0,0,0,0.35);
  }
  .brand-name {
    font-family: "Poppins", sans-serif;
    font-weight: 500;
    font-size: 40px;
    letter-spacing: 4px;
    fill: var(--ink);
  }
  .headline {
    font-family: "Saira Condensed", sans-serif;
    font-style: italic;
    font-weight: 800;
    font-size: 80px;
    fill: var(--paper);
  }
  .feature-text {
    font-family: "Poppins", sans-serif;
    font-weight: 400;
    font-size: 23px;
    fill: var(--text);
  }
  .cta-lead {
    font-family: "Poppins", sans-serif;
    font-weight: 600;
    font-size: 25px;
    fill: var(--paper);
  }
  .cta-url {
    font-family: "Poppins", sans-serif;
    font-weight: 400;
    font-size: 29px;
    fill: var(--paper);
  }
  .tick-badge { fill: var(--brand-red); }
  .tick-mark { fill: none; stroke: var(--paper); stroke-width: 3; stroke-linecap: round; stroke-linejoin: round; }
</style>
</head>
<body>
<svg class="flyer" viewBox="0 0 1128 1583" xmlns="http://www.w3.org/2000/svg">
  <defs>
    <linearGradient id="heroTone" x1="0" y1="0" x2="1" y2="1">
      <stop offset="0" stop-color="#c9c6c2"/>
      <stop offset="0.45" stop-color="#3b3b3d"/>
      <stop offset="1" stop-color="#1e1d1f"/>
    </linearGradient>
    <linearGradient id="fleetTone" x1="0" y1="0" x2="0" y2="1">
      <stop offset="0" stop-color="#d9d6d2"/>
      <stop offset="0.55" stop-color="#6d6c6e"/>
      <stop offset="1" stop-color="#cdbfb6"/>
    </linearGradient>
    <linearGradient id="crewTone" x1="0" y1="0" x2="0" y2="1">
      <stop offset="0" stop-color="#6f95c2"/>
      <stop offset="0.45" stop-color="#4a4a4e"/>
      <stop offset="1" stop-color="#1c1c1e"/>
    </linearGradient>
    <clipPath id="fleetClip"><circle cx="338" cy="685" r="126"/></clipPath>
    <clipPath id="crewClip"><circle cx="541" cy="722" r="101"/></clipPath>
  </defs>

  <rect class="paper" width="1128" height="1583" fill="var(--paper)"/>

  <!-- hero photograph area -->
  <rect class="hero-photo" role="img" aria-label="Uniformed chauffeur assisting a business traveler with luggage beside a black SUV" x="0" y="0" width="1128" height="800" fill="url(#heroTone)"/>

  <!-- red heading blob -->
  <path class="hero-red" fill="var(--brand-red)"
        d="M0,255 C250,240 430,150 545,10 C430,120 400,240 455,340 C515,440 520,560 470,620 C420,680 300,700 0,630 Z"/>

  <!-- top white logo area and black band -->
  <path class="top-band" fill="var(--ink)"
        d="M0,238 C300,215 480,110 562,0 L552,0 C470,150 300,260 0,275 Z"/>
  <path class="top-white" fill="var(--paper)"
        d="M0,0 L562,0 C480,110 300,215 0,238 Z"/>

  <!-- lower hero swooshes -->
  <path class="swoosh-red" fill="var(--brand-red)"
        d="M480,770 C750,760 980,690 1128,585 L1128,640 C980,730 760,780 480,790 Z"/>
  <path class="swoosh-black" fill="var(--ink)"
        d="M0,640 C200,720 450,770 700,775 C900,775 1050,710 1128,650 L1128,700 C1000,760 820,790 650,790 C420,790 200,760 0,700 Z"/>
  <path class="swoosh-white-line" fill="none" stroke="var(--paper)" stroke-width="10"
        d="M0,622 C200,705 450,758 700,762 C900,762 1050,700 1128,640"/>
  <path class="lower-white" fill="var(--paper)"
        d="M0,700 C200,760 420,790 650,790 C820,790 1000,760 1128,700 L1128,1583 L0,1583 Z"/>
  <path class="swoosh-red-thin" fill="var(--brand-red)"
        d="M680,778 C880,770 1030,720 1128,680 L1128,690 C1030,735 880,775 680,780 Z"/>

  <!-- brand name -->
  <text class="brand-name" x="228" y="158" text-anchor="middle">ROVANDEL</text>
  <line x1="140" y1="180" x2="316" y2="180" stroke="var(--brand-red)" stroke-width="1.5"/>

  <!-- headline -->
  <text class="headline">
    <tspan x="76" y="365">DALLAS TO</tspan>
    <tspan x="76" y="432">AUSTIN</tspan>
    <tspan x="76" y="499">CHAUFFEURED</tspan>
    <tspan x="76" y="566">SUVS</tspan>
  </text>

  <!-- photo circles -->
  <circle cx="338" cy="685" r="132" fill="var(--ink)"/>
  <rect class="fleet-photo" role="img" aria-label="Chauffeurs standing beside a fleet of SUVs in front of a building" x="200" y="550" width="280" height="270" fill="url(#fleetTone)" clip-path="url(#fleetClip)"/>
  <circle cx="541" cy="722" r="107" fill="var(--ink)"/>
  <rect class="crew-photo" role="img" aria-label="Group of uniformed chauffeurs in caps" x="430" y="615" width="225" height="215" fill="url(#crewTone)" clip-path="url(#crewClip)"/>

  <!-- feature list, left column -->
  <g class="feature-list">
    <g class="tick"><circle class="tick-badge" cx="80" cy="868" r="12"/><path class="tick-mark" d="M74,868 l4,4 l8,-8"/></g>
    <text class="feature-text"><tspan x="107" y="877">Travel Dallas to Austin in a new 2025</tspan><tspan x="107" y="906">Morvan Tessell for $499 one way</tspan></text>

    <g class="tick"><circle class="tick-badge" cx="80" cy="963" r="12"/><path class="tick-mark" d="M74,963 l4,4 l8,-8"/></g>
    <text class="feature-text"><tspan x="107" y="972">Trip includes a Uniformed</tspan><tspan x="107" y="1001">Chauffeur who has a Commercial</tspan><tspan x="107" y="1030">Drivers License (CDL)</tspan></text>

    <g class="tick"><circle class="tick-badge" cx="80" cy="1083" r="12"/><path class="tick-mark" d="M74,1083 l4,4 l8,-8"/></g>
    <text class="feature-text"><tspan x="107" y="1092">You can Schedule Chauffeur</tspan><tspan x="107" y="1121">Pickup at Your Home in Dallas</tspan></text>

    <g class="tick"><circle class="tick-badge" cx="80" cy="1166" r="12"/><path class="tick-mark" d="M74,1166 l4,4 l8,-8"/></g>
    <text class="feature-text"><tspan x="107" y="1175">Our Chauffeur will Drop You Off</tspan><tspan x="107" y="1204">at Your Final Destination in Austin</tspan></text>

    <g class="tick"><circle class="tick-badge" cx="80" cy="1256" r="12"/><path class="tick-mark" d="M74,1256 l4,4 l8,-8"/></g>
    <text class="feature-text"><tspan x="107" y="1265">You can Schedule Chauffeur</tspan><tspan x="107" y="1294">Return Pickup in Austin and</tspan><tspan x="107" y="1323">Return Back to Dallas.</tspan></text>

    <g class="tick"><circle class="tick-badge" cx="80" cy="1376" r="12"/><path class="tick-mark" d="M74,1376 l4,4 l8,-8"/></g>
    <text class="feature-text"><tspan x="107" y="1385">We offer Faster Times on Door-</tspan><tspan x="107" y="1414">to-Door Travel than Quillbrook</tspan><tspan x="107" y="1443">Airways</tspan></text>
  </g>

  <!-- feature list, right column -->
  <g class="feature-list">
    <g class="tick"><circle class="tick-badge" cx="599" cy="865" r="12"/><path class="tick-mark" d="M593,865 l4,4 l8,-8"/></g>
    <text class="feature-text"><tspan x="628" y="874">We offer Comparable Prices</tspan><tspan x="628" y="903">on Door-to-Door Travel Times</tspan><tspan x="628" y="932">than Quillbrook Airways</tspan></text>

    <g class="tick"><circle class="tick-badge" cx="599" cy="982" r="12"/><path class="tick-mark" d="M593,982 l4,4 l8,-8"/></g>
    <text class="feature-text"><tspan x="628" y="989">All of our trips are insured with $500k</tspan><tspan x="628" y="1018">of commercial auto insurance</tspan></text>

    <g class="tick"><circle class="tick-badge" cx="599" cy="1067" r="12"/><path class="tick-mark" d="M593,1067 l4,4 l8,-8"/></g>
    <text class="feature-text"><tspan x="628" y="1076">Our Passengers can Talk on Cell</tspan><tspan x="628" y="1105">Phone &amp; Conduct Plinko calls</tspan><tspan x="628" y="1134">Throughout Travel</tspan></text>

    <g class="tick"><circle class="tick-badge" cx="599" cy="1182" r="12"/><path class="tick-mark" d="M593,1182 l4,4 l8,-8"/></g>
    <text class="feature-text"><tspan x="628" y="1191">Our Passengers have Maximum</tspan><tspan x="628" y="1220">Privacy, Comfort and First-Class</tspan><tspan x="628" y="1249">Amenities.</tspan></text>

    <g class="tick"><circle class="tick-badge" cx="599" cy="1297" r="12"/><path class="tick-mark" d="M593,1297 l4,4 l8,-8"/></g>
    <text class="feature-text"><tspan x="628" y="1306">Our Passengers Avoid Harwick Meadow</tspan><tspan x="628" y="1335">Airfield and KRN Airport hassles</tspan><tspan x="628" y="1364">&amp; delays</tspan></text>

    <g class="tick"><circle class="tick-badge" cx="599" cy="1383" r="12"/><path class="tick-mark" d="M593,1383 l4,4 l8,-8"/></g>
    <text class="feature-text"><tspan x="628" y="1392">Member Brixley Chamber of</tspan><tspan x="628" y="1421">Commerce, Fenmore Chamber of</tspan><tspan x="628" y="1450">Commerce.</tspan></text>
  </g>

  <!-- footer -->
  <path class="footer-red" fill="var(--brand-red)"
        d="M0,1510 C130,1490 280,1480 412,1474 C280,1488 140,1515 0,1550 Z"/>
  <path class="footer-band" fill="var(--ink)"
        d="M0,1558 C300,1470 700,1455 1128,1550 L1128,1583 L0,1583 Z"/>
  <text x="565" y="1541" text-anchor="middle"><tspan class="cta-lead">Book your trip today at</tspan><tspan class="cta-url" dx="22">www.rovandel.example</tspan></text>
</svg>
</body>
</html>
```